tourism marketplace web app redesign*

Hi, I need our front-page redesigned. For the competition please submit a jpg of ABOVE THE FOLD ONLY. The full page redesign will be a revision request. URL is https://qp.trolvexa.hu/hu/index.html login:'fullhd' and password:'asdasd' (Fold is supposed to be at "Kiemelt Ajanlatok", use all elements above that. Please use at least one extra color other than the two in the logo, or you may completely change them. FOCUS should be on the central combined search box (3 dropdown, 2 calendar picker + Kereses Button) just like nestorly.com, ravimoto.com, Pelusi.com, etc... The search box is always large, central, white, we want that too. We want it to look more modern, more clean AND we want to feature a changing beautiful nature photo background (like nestorly.com).Please use our newly designed logo (in attached pdf) and use that new spelling: "ferntrail.online"

```html
<!DOCTYPE html>
<html lang="hu">
<head>
<meta charset="UTF-8">
<title>ferntrail.online – Vadászat közvetlenül</title>
<link rel="stylesheet" href="https://fonts.googleapis.com/css2?family=Poppins:wght@400;500&display=swap">
<style>
  :root {
    --green: #5c9e87;
    --green-light: #7ab29f;
    --ink: #2b2f2d;
    --muted: #4d5a55;
    --white: #ffffff;
    --field-bg: rgba(248, 248, 247, 0.92);
    --card-bg: rgba(255, 255, 255, 0.86);
  }
  * { box-sizing: border-box; margin: 0; padding: 0; }
  html, body { width: 1200px; height: 675px; overflow: hidden; }
  body {
    font-family: "Poppins", sans-serif;
    color: var(--ink);
    position: relative;
  }
  .hero-photo {
    position: absolute; inset: 0;
    background:
      radial-gradient(ellipse at 80% 75%, #2f4a3f 0%, rgba(47,74,63,0.6) 35%, rgba(47,74,63,0) 65%),
      linear-gradient(170deg, #eef0f0 0%, #dfe3e3 30%, #b7c2bd 55%, #6e8479 80%, #4b6258 100%);
  }
  .site-header {
    position: absolute; left: 0; top: 0; width: 1200px; height: 72.5px;
    background: rgba(255,255,255,0.55);
  }
  .brand {
    position: absolute; left: 46px; top: 17px; height: 47px;
    display: flex; align-items: center; gap: 10px;
  }
  .brand-dot { width: 47px; height: 47px; border-radius: 50%; background: var(--green); }
  .brand-name { font-size: 21px; font-weight: 500; color: var(--green); }
  .utility-nav {
    position: absolute; right: 56px; top: 28px;
    display: flex; align-items: center; gap: 16px;
    font-size: 13px; color: var(--muted);
  }
  .utility-nav .caret { font-size: 10px; margin-left: 2px; }
  .account { display: flex; align-items: center; gap: 5px; }
  .main-nav {
    position: absolute; left: 0; top: 72.5px; width: 1200px; height: 49.5px;
    background: var(--green);
  }
  .main-nav .active-bg {
    position: absolute; left: 146px; top: 0; width: 130px; height: 49.5px;
    background: var(--green-light);
  }
  .main-nav a {
    position: absolute; top: 0; line-height: 49.5px;
    transform: translateX(-50%);
    color: var(--white); font-size: 13px; font-weight: 500; text-decoration: none; white-space: nowrap;
  }
  .hero-title {
    position: absolute; left: 46px; top: 138px;
    font-size: 30px; font-weight: 500; color: var(--green); letter-spacing: 0.2px;
  }
  .hero-sub {
    position: absolute; left: 46px; top: 176px;
    font-size: 15px; font-weight: 500; color: var(--ink);
  }
  .category-pill {
    position: absolute; top: 207px; height: 42px; border-radius: 21px;
    background: var(--green); color: var(--white);
    font-size: 12.5px; font-weight: 500;
    display: flex; align-items: center; justify-content: center;
  }
  .search-card {
    position: absolute; left: 46px; top: 286px; width: 520px; height: 338px;
    border-radius: 31px; background: var(--card-bg);
  }
  .field-label {
    position: absolute; left: 63px; font-size: 14px; color: var(--ink); line-height: 42px;
  }
  .select-field, .date-field {
    position: absolute; height: 42px; border-radius: 21px;
    border: 1px solid var(--green); background: var(--field-bg);
  }
  .select-field { left: 198px; width: 260px; }
  .select-field::after {
    content: "▼"; position: absolute; right: 16px; top: 12px;
    font-size: 10px; color: var(--green);
  }
  .date-from { left: 63px; top: 183px; width: 180px; }
  .date-to { left: 277px; top: 183px; width: 181px; }
  .range-arrow { position: absolute; left: 250px; top: 196px; }
  .search-stats {
    position: absolute; left: 170px; top: 239px; right: 62px;
    display: flex; align-items: center; font-size: 9.5px; color: var(--ink);
  }
  .search-stats span { display: flex; align-items: center; gap: 2px; margin-right: 8px; }
  .search-stats .sort { margin-left: auto; margin-right: 0; }
  .search-button {
    position: absolute; left: 319px; top: 278px; width: 139px; height: 42px;
    border-radius: 21px; border: none; background: var(--green); color: var(--white);
    font-family: "Poppins", sans-serif; font-size: 15px; font-weight: 500;
  }
  .slide-dots { position: absolute; left: 241px; top: 644px; display: flex; gap: 9.5px; }
  .slide-dots i { width: 12px; height: 12px; border-radius: 50%; background: rgba(255,255,255,0.9); display: block; }
  .slide-dots i.current { background: #d6d9d8; }
</style>
</head>
<body>
  <div class="hero-photo" role="img" aria-label="Ködös fenyőerdő háttérfotó"></div>

  <header class="site-header">
    <div class="brand">
      <span class="brand-dot"></span>
      <span class="brand-name">ferntrail.online</span>
    </div>
    <nav class="utility-nav">
      <span>Large</span>
      <span>Magyar<span class="caret">▼</span></span>
      <span>EUR<span class="caret">▼</span></span>
      <span class="account">
        <svg width="13" height="15" viewBox="0 0 13 15" fill="none" stroke="#4d5a55" stroke-width="1.2"><circle cx="6.5" cy="4.5" r="3.5"/><path d="M1 14c0-3.2 2.5-5.3 5.5-5.3S12 10.8 12 14"/></svg>
        Regisztráció / Bejelentkezés
      </span>
    </nav>
  </header>

  <nav class="main-nav">
    <span class="active-bg"></span>
    <a href="#" style="left:211px">Országok</a>
    <a href="#" style="left:346px">Vadfajok</a>
    <a href="#" style="left:477px">Rólunk</a>
    <a href="#" style="left:595px">ÁSZF</a>
    <a href="#" style="left:744px">Hogyan működik</a>
    <a href="#" style="left:951px">+ Legyen partnerünk</a>
  </nav>

  <h1 class="hero-title">Nincs szükséged vadászatszervezőre!</h1>
  <p class="hero-sub">Foglalj közvetlen a vadászterületnél</p>

  <a class="category-pill" style="left:46px;width:146px">Egyéni vadászatok</a>
  <a class="category-pill" style="left:204px;width:208px">Társas vadászatok, hajtások</a>
  <a class="category-pill" style="left:425px;width:141px">Exkluzív csomagok</a>

  <form class="search-card">
    <label class="field-label" style="top:20px">összes vad</label>
    <div class="select-field" style="top:20px"></div>
    <label class="field-label" style="top:70px">összes ország</label>
    <div class="select-field" style="top:70px"></div>
    <label class="field-label" style="top:119px">összes ajánlat</label>
    <div class="select-field" style="top:119px"></div>

    <div class="date-field date-from"></div>
    <svg class="range-arrow" width="20" height="12" viewBox="0 0 20 12" fill="none" stroke="#5c9e87" stroke-width="1.3"><path d="M1 6h18M5 2L1 6l4 4M15 2l4 4-4 4"/></svg>
    <div class="date-field date-to"></div>

    <div class="search-stats">
      <span>
        <svg width="8" height="10" viewBox="0 0 8 10" fill="none" stroke="#2b2f2d" stroke-width="0.8"><path d="M4 9.5S7.5 6 7.5 4A3.5 3.5 0 0 0 .5 4C.5 6 4 9.5 4 9.5z"/><circle cx="4" cy="4" r="1.2"/></svg>
        123456 terület
      </span>
      <span>
        <svg width="10" height="10" viewBox="0 0 10 10" fill="none" stroke="#2b2f2d" stroke-width="0.8"><circle cx="5" cy="5" r="4"/><circle cx="5" cy="5" r="2.5"/></svg>
        87654321 ajánlat
      </span>
      <span class="sort">Rendezés keresés</span>
    </div>

    <button type="button" class="search-button">keresés</button>
  </form>

  <div class="slide-dots">
    <i class="current"></i><i></i><i></i><i></i><i></i>
  </div>
</body>
</html>
```